Wexmoor Digest - our client magazine

A quality magazine consisting of a number of bespoke articles in the first half followed by an overview of each company that form part of the group as well as details of the services offered. Vast majority of the copy is attached to provide a good overview of the content required. The magazine will require printing so quality imagery is required.

Industry/Entity Type

Recruitment

Font styles to use
Serif

Colors
0355a3
6b449b
3276b5
876aae
a64599
00a990
5c5c5c
000000
474747

Requirements
Must have
• Bringing the copy to life through flow charts and/or diagrams where possible.

```html
<!DOCTYPE html>
<html lang="en">
<head>
<meta charset="utf-8">
<title>Wexmoor Digest – Spread 4–5</title>
<link href="https://fonts.googleapis.com/css2?family=Cormorant+Garamond:ital,wght@0,400;0,500;0,600;0,700;1,400&family=Josefin+Sans:wght@300&display=swap" rel="stylesheet">
<style>
  :root {
    --band: #c4c4c4;
    --paper: #ffffff;
    --ink: #000000;
    --text: #2b2b2b;
    --rule: #8a8a8a;
    --muted: #5c5c5c;
    --accent: #7ed321;
  }
  * { margin: 0; padding: 0; box-sizing: border-box; }
  html, body { width: 1200px; height: 803px; overflow: hidden; background: var(--paper); }
  .spread { position: relative; width: 1200px; height: 803px; background: var(--paper); font-family: "Cormorant Garamond", Georgia, serif; color: var(--text); }
  .band { position: absolute; left: 0; width: 1200px; background: var(--band); }
  .band--top { top: 0; height: 13px; }
  .band--bottom { top: 790px; height: 13px; }

  .masthead { position: absolute; font-family: "Josefin Sans", Arial, sans-serif; font-weight: 300; font-size: 13px; letter-spacing: 5px; color: var(--muted); white-space: nowrap; display: flex; align-items: center; gap: 10px; }
  .masthead__mark { width: 9px; height: 9px; background: var(--accent); }
  .masthead--left { left: 44px; top: 282px; transform-origin: 0 0; transform: rotate(-90deg); }
  .masthead--right { left: 1165px; top: 96px; transform-origin: 0 0; transform: rotate(90deg); }

  .entry { position: absolute; left: 98px; width: 420px; }
  .entry__head { display: flex; align-items: baseline; height: 22px; border-bottom: 1px solid var(--rule); }
  .entry__num { width: 116px; font-size: 10px; font-weight: 700; letter-spacing: 1px; }
  .entry__title { font-size: 11.5px; font-weight: 700; letter-spacing: 1.6px; text-transform: uppercase; }
  .entry__body { margin: 18px 0 0 116px; font-size: 11.5px; line-height: 17.6px; letter-spacing: 0.9px; }
  .entry__body em { font-style: italic; }

  .folio { position: absolute; top: 753px; font-size: 11px; }

  .feature-image { position: absolute; left: 693px; top: 96px; width: 407px; height: 184px; background: var(--ink); }
  .feature-title { position: absolute; left: 693px; top: 292px; width: 407px; font-size: 23px; font-weight: 500; line-height: 28px; color: #222; }
  .feature-copy { position: absolute; left: 693px; top: 366px; width: 407px; font-size: 11.2px; color: var(--text); }
  .feature-copy .lead { line-height: 15.6px; letter-spacing: 0.6px; text-align: justify; margin-bottom: 15px; }
  .feature-copy .step { font-size: 11.5px; letter-spacing: 0.4px; line-height: 13px; }
  .feature-copy p, .feature-copy li { line-height: 13.8px; text-align: justify; }
  .feature-copy ul { list-style: none; margin-top: 13px; }
  .feature-copy li { margin-bottom: 13.5px; }
  .feature-copy li::before { content: "•"; margin-right: 8px; }
  .feature-copy li:last-child { margin-bottom: 0; }
</style>
</head>
<body>
<div class="spread">
  <div class="band band--top"></div>
  <div class="band band--bottom"></div>

  <div class="masthead masthead--left"><span class="masthead__mark"></span>WEXMOOR DIGEST</div>

  <section class="entry" style="top:90px">
    <div class="entry__head"><span class="entry__num">24.</span><span class="entry__title">Ibusame nosam voloruntur</span></div>
    <p class="entry__body"><em>Nulpa corem nonseculla nulparum</em><br>doluptiis essitat emquidiande officit hit a con<br>rempori orectus daecerion cum ipsam qui.</p>
  </section>
  <section class="entry" style="top:263px">
    <div class="entry__head"><span class="entry__num">26.</span><span class="entry__title">El mo optiaspedit</span></div>
    <p class="entry__body">Ehenda simollat. Epudand aernati beaquibusa<br>comnihit eleste pelles es molorer rundant provid<br>modigenis secature.</p>
  </section>
  <section class="entry" style="top:436px">
    <div class="entry__head"><span class="entry__num">28.</span><span class="entry__title">Apicitate eum quis</span></div>
    <p class="entry__body">Nam numquatus doleceatio. Ut enecerovit labo. At<br>raeperitate vent.<br><em>Ihillen ihilluptam, sequatiatem ex et aut omnitis</em></p>
  </section>
  <section class="entry" style="top:609px">
    <div class="entry__head"><span class="entry__num">29.</span><span class="entry__title">Igent occaepro berum</span></div>
    <p class="entry__body">Repelique nonsect umquam quidit veliquam, apelest,<br>ni rem eos eum qui utatem aliquam natiand ipisciis<br>doluptas dio vellatu samus.</p>
  </section>

  <div class="folio" style="left:297px">4</div>

  <div class="feature-image" role="img" aria-label="Feature photograph for the employee value proposition article"></div>
  <h1 class="feature-title">4 steps to a unique &amp; compelling<br>Employee Value Proposition</h1>
  <div class="feature-copy">
    <p class="lead">A truly unique and compelling Employee Value Proposition (EVP) is vital for any organisation looking to attract and retain top talent. It is important that it is a true representation of your company culture and attitudes to staff, and that it aligns with the strategic vision for the business. Here are our 4 simple steps to follow to create a great EVP:</p>
    <div class="step">1.&nbsp; Agree your goals</div>
    <p>First you need to have clear goals for recruitment and retention in your business so that you can specify how your EVP should support these. The following questions are likely to be helpful:</p>
    <ul>
      <li>What are the long term strategic goals for the business which need to be supported by your recruitment and retention practices?</li>
      <li>What are the key recruitment challenges your organisation is facing?</li>
      <li>What candidate persona are you trying to attract?</li>
      <li>What candidate persona are you trying to retain? If this is different from the persona you are trying to attract then why is this the case?</li>
      <li>How do you expect your EVP to help the business?</li>
    </ul>
    <p>Once you understand why you need to recruit and retain top talent, it becomes easier to define why you are developing an EVP and what it is being designed to achieve.</p>
  </div>

  <div class="masthead masthead--right"><span class="masthead__mark"></span>WEXMOOR DIGEST</div>

  <div class="folio" style="left:897px">5</div>
</div>
</body>
</html>
```